Lavoie Roofing

Want a professional looking business card

Industry/Entity Type

Business

Contact Information for Business Card

Mark Lavoie ( Owner) mark@lavoieroofing.example, www.lavoieroofing.example, Adress: 4712 Cedar Ridge road 31 Maplebrook, NB E9Z2M4

```html
<!DOCTYPE html>
<html lang="en">
<head>
<meta charset="utf-8">
<title>Lavoie Roofing – Business Card</title>
<link href="https://fonts.googleapis.com/css2?family=Exo+2:wght@400;600;800&display=swap" rel="stylesheet">
<style>
  :root {
    --stage: #111111;
    --card: #1a1a1b;
    --card-edge: #242425;
    --brand-blue: #2456b3;
    --text-grey: #8a8a8c;
    --text-light: #a9a9ab;
  }
  * { box-sizing: border-box; margin: 0; padding: 0; }
  html, body {
    width: 1200px;
    height: 1000px;
    overflow: hidden;
    background: var(--stage);
    font-family: "Exo 2", sans-serif;
  }
  .card-set {
    position: absolute;
    top: 350px;
    left: 50px;
    display: flex;
    gap: 50px;
  }
  .card {
    position: relative;
    width: 525px;
    height: 300px;
    background: var(--card);
    border: 1px solid var(--card-edge);
    box-shadow: 0 20px 40px rgba(0,0,0,0.6);
    overflow: hidden;
  }
  .brand-name {
    display: flex;
    align-items: center;
    gap: 10px;
    font-weight: 800;
    color: var(--brand-blue);
    text-transform: uppercase;
    letter-spacing: 2px;
    white-space: nowrap;
    line-height: 1;
  }
  .brand-mark {
    width: 14px;
    height: 14px;
    background: var(--brand-blue);
    flex: none;
  }
  .card--front .brand-name {
    position: absolute;
    top: 50%;
    left: 50%;
    transform: translate(-50%, -50%);
    font-size: 36px;
  }
  .card--back .brand-name {
    position: absolute;
    top: 122px;
    right: 34px;
    font-size: 26px;
  }
  .holder {
    position: absolute;
    top: 34px;
    left: 34px;
    line-height: 1.05;
  }
  .holder-name {
    font-size: 22px;
    font-weight: 600;
    color: var(--text-light);
  }
  .holder-name .first { color: var(--brand-blue); }
  .holder-title {
    font-size: 17px;
    color: var(--text-grey);
  }
  .contact-online {
    position: absolute;
    top: 168px;
    left: 34px;
    font-size: 15px;
    line-height: 1.45;
    color: var(--text-grey);
  }
  .address {
    position: absolute;
    right: 34px;
    bottom: 38px;
    font-size: 17px;
    font-style: normal;
    line-height: 1.3;
    color: var(--text-light);
    text-align: right;
  }
  .accent-band {
    position: absolute;
    left: 0;
    right: 0;
    bottom: 0;
    height: 14px;
    background: var(--brand-blue);
  }
</style>
</head>
<body>
  <main class="card-set">
    <section class="card card--front" aria-label="Card front">
      <div class="brand-name"><span class="brand-mark"></span>Lavoie Roofing</div>
    </section>

    <section class="card card--back" aria-label="Card back">
      <div class="holder">
        <p class="holder-name"><span class="first">Mark</span> Lavoie</p>
        <p class="holder-title">Owner</p>
      </div>
      <div class="brand-name"><span class="brand-mark"></span>Lavoie Roofing</div>
      <div class="contact-online">
        <p>mark@lavoieroofing.example</p>
        <p>www.lavoieroofing.example</p>
      </div>
      <address class="address">
        <p>4712 Cedar Ridge road 31,</p>
        <p>Maplebrook, NB E9Z2M4</p>
      </address>
      <div class="accent-band"></div>
    </section>
  </main>
</body>
</html>
```